3" Round Business Card for Funeral Home

We need a business card designed for our cremation service. We would like to use a 3" round business card.

The business card will be 2-sided. One side with the logo featured prominently. The back sad will have employee name and contact info.

Templates for printing have been attached to project as well as logo

We like soft colors like the logo. Final design should promote a feeling of trust.

Industry/Entity Type

Funeral

Contact Information for Business Card

Employee Name, Phone number, email, web address

Requirements
Should not have
• any sort of funeral item such as urn, casket, hearse, tombstone

```html
<!DOCTYPE html>
<html lang="en">
<head>
<meta charset="utf-8">
<title>Stillwater Rest – Round Business Card</title>
<link rel="stylesheet" href="https://fonts.googleapis.com/css2?family=Montserrat:wght@400;600;700;800&display=swap">
<style>
  :root {
    --teal: #1ea69a;
    --plum: #8e2c8a;
    --ink: #0b0b0b;
    --paper: #ffffff;
    --mist-light: #f1f1f1;
    --mist-mid: #dcdcdc;
    --mist-dark: #c4c4c4;
  }
  * { margin: 0; padding: 0; box-sizing: border-box; }
  html, body {
    width: 1200px; height: 593px; overflow: hidden;
    background: var(--paper);
    font-family: "Montserrat", sans-serif;
  }
  .canvas { position: relative; width: 1200px; height: 593px; }
  .card-side {
    position: absolute; top: 3px; width: 594px; height: 587px; overflow: hidden;
  }
  .card-front { left: 4px; }
  .card-reverse { left: 603px; }
  .backdrop { position: absolute; inset: 0; }
  .card-front .backdrop {
    background: linear-gradient(150deg, var(--mist-light) 0%, var(--mist-light) 30%, var(--mist-mid) 60%, var(--mist-dark) 100%);
  }
  .card-reverse .backdrop {
    background: radial-gradient(ellipse at 50% 45%, var(--mist-light) 0%, var(--mist-mid) 55%, var(--mist-dark) 100%);
  }
  .frame { position: absolute; left: 0; top: 0; width: 594px; height: 587px; }
  .brand-name {
    position: absolute; left: 0; right: 0; text-align: center;
    color: var(--teal); font-weight: 400; letter-spacing: -0.5px; line-height: 1;
  }
  .card-front .brand-name { top: 258px; font-size: 44px; }
  .card-reverse .brand-name { top: 163px; font-size: 29px; }
  .tagline {
    position: absolute; left: 0; right: 0; top: 389px; text-align: center;
    color: var(--teal); font-weight: 700; font-size: 20px; letter-spacing: 4px; line-height: 1;
  }
  .employee-name {
    position: absolute; left: 0; right: 0; top: 245px; text-align: center;
    color: var(--ink); font-weight: 800; font-size: 36px; letter-spacing: 3.5px; line-height: 1;
  }
  .contact-list { list-style: none; }
  .contact-item {
    position: absolute; left: 202px; white-space: nowrap;
    color: var(--ink); font-weight: 700; font-size: 12.5px; letter-spacing: 3.6px; line-height: 1;
    transform: translateY(-50%);
  }
  .contact-phone { top: 343px; }
  .contact-email { top: 385px; }
  .contact-web { top: 424px; }
</style>
</head>
<body>
<div class="canvas">

  <section class="card-side card-front">
    <div class="backdrop" role="img" aria-label="Soft grey halftone photograph of white flowers"></div>
    <svg class="frame" viewBox="0 0 594 587" aria-hidden="true">
      <g fill="none" stroke="var(--plum)" stroke-width="2.5">
        <polyline points="155,232 155,149 439,149 439,232"/>
        <polyline points="155,350 155,433 439,433 439,350"/>
      </g>
    </svg>
    <div class="brand-name">stillwaterrest.com</div>
    <div class="tagline">Funeral Home</div>
  </section>

  <section class="card-side card-reverse">
    <div class="backdrop" role="img" aria-label="Soft grey halftone photograph of white flowers"></div>
    <svg class="frame" viewBox="0 0 594 587" aria-hidden="true">
      <g fill="none" stroke="var(--plum)" stroke-width="2.5">
        <polyline points="117,234 117,114 480,114 480,234"/>
        <polyline points="117,316 117,482 480,482 480,316"/>
        <line x1="100" y1="298" x2="496" y2="298"/>
      </g>
      <g fill="none" stroke="var(--teal)" stroke-width="1.8" stroke-linejoin="round">
        <rect x="158" y="323" width="19" height="35" rx="3"/>
        <rect x="161" y="329" width="13" height="22" rx="1"/>
        <circle cx="167.5" cy="354" r="1.3" fill="var(--teal)"/>
        <rect x="148" y="372" width="35" height="25" rx="1"/>
        <polyline points="148,373 165.5,387 183,373"/>
        <path d="M167.5 443 C160 431 156 425 156 418 A11.5 11.5 0 0 1 179 418 C179 425 175 431 167.5 443 Z"/>
        <circle cx="167.5" cy="417" r="4.5"/>
      </g>
    </svg>
    <div class="brand-name">stillwaterrest.com</div>
    <div class="employee-name">Employee Name</div>
    <ul class="contact-list">
      <li class="contact-item contact-phone">+0555018274</li>
      <li class="contact-item contact-email">hello@stillwaterrest.com</li>
      <li class="contact-item contact-web">stillwaterrest.com</li>
    </ul>
  </section>

</div>
</body>
</html>
```